Business card for a shop called "Bright pine company"

the shop are selling disposable wooden packaging cutlery, wooden trays, wooden plates, carton, box, adhesive, stretch film...
Fully recyclable and 100% wood.
We want something futuristic and good for the planet

Target Market(s)

professional customers, company, fast-food, restaurant, caterer,

Industry/Entity Type

wood furnitures for food

Contact Information for Business Card

Colors

Designer to choose colors to be used in the design.

Requirements
Must have
• QR CODE, selective varnish on the given logo, brown and neon green light color. Name and surname, function (CEO), tel, mail and address.
Nice to have
• minimalist design , futuristic and ecology
Should not have
• the list of furniture we are selling.

```html
<!DOCTYPE html>
<html lang="en">
<head>
<meta charset="utf-8">
<title>Bright pine company — Business Card</title>
<link rel="stylesheet" href="https://fonts.googleapis.com/css2?family=Mulish:wght@400;600&family=Arimo:wght@400&display=swap">
<style>
  :root {
    --stage: #ececec;
    --card-light: #ffffff;
    --card-dark: #1f1f1f;
    --edge-brown: #8a5d14;
    --brand-green: #1f9a3c;
    --neon-green: #6cff6a;
    --ink: #1c1c1c;
    --rule: #8c8c8c;
    --white: #ffffff;
  }
  * { box-sizing: border-box; margin: 0; padding: 0; }
  html, body { width: 1200px; height: 900px; overflow: hidden; }
  body { background: var(--stage); position: relative; font-family: "Arimo", Arial, sans-serif; }

  .card {
    position: absolute;
    width: 700px;
    height: 400px;
    border-bottom: 3px solid var(--edge-brown);
    border-left: 2px solid var(--edge-brown);
    box-shadow: 0 10px 28px rgba(0,0,0,0.22);
  }

  /* Front side */
  .card--front { left: 110px; top: 40px; background: var(--card-light); }
  .identity { position: absolute; left: 0; right: 0; top: 108px; text-align: center; }
  .identity__name { font-family: "Mulish", sans-serif; font-weight: 600; font-size: 34px; color: var(--brand-green); letter-spacing: 0.3px; }
  .identity__role { font-size: 17px; color: var(--ink); margin-top: 2px; }

  .details { position: absolute; top: 200px; left: 0; right: 0; display: flex; justify-content: center; gap: 24px; }
  .details__address { text-align: right; font-size: 18px; line-height: 1.4; color: var(--ink); padding-top: 8px; }
  .details__rule { width: 1px; background: var(--rule); height: 92px; }
  .contact { list-style: none; font-size: 18px; line-height: 1.4; color: var(--ink); }
  .contact li { display: flex; align-items: center; gap: 8px; }
  .contact svg { width: 17px; height: 17px; fill: var(--brand-green); flex: none; }
  .contact .accent { color: var(--brand-green); }

  /* Back side */
  .card--back { left: 390px; top: 470px; background: var(--card-dark); }
  .brand { position: absolute; left: 0; right: 0; top: 135px; display: flex; justify-content: center; align-items: center; gap: 14px; }
  .brand__dot { width: 22px; height: 22px; border-radius: 50%; background: var(--neon-green); }
  .brand__name { font-family: "Mulish", sans-serif; font-weight: 600; font-size: 40px; color: var(--neon-green); }

  .pledge { position: absolute; left: 90px; bottom: 52px; display: flex; align-items: center; gap: 22px; }
  .pledge__badge { width: 58px; height: 58px; border-radius: 50%; background: var(--brand-green); }
  .pledge__text { font-size: 22px; color: var(--white); letter-spacing: 1px; }
</style>
</head>
<body>

<section class="card card--front" aria-label="Business card front">
  <header class="identity">
    <h1 class="identity__name">Daniel Harper</h1>
    <p class="identity__role">Managing Director</p>
  </header>
  <div class="details">
    <address class="details__address" style="font-style:normal">
      88, Cedar Lane<br>Harbor Town 30817<br>Northland
    </address>
    <div class="details__rule"></div>
    <ul class="contact">
      <li>
        <svg viewBox="0 0 24 24" aria-hidden="true"><path d="M6.6 10.8a15.1 15.1 0 0 0 6.6 6.6l2.2-2.2a1 1 0 0 1 1-.25 11.4 11.4 0 0 0 3.6.57 1 1 0 0 1 1 1V20a1 1 0 0 1-1 1A17 17 0 0 1 3 4a1 1 0 0 1 1-1h3.5a1 1 0 0 1 1 1c0 1.25.2 2.45.57 3.57a1 1 0 0 1-.25 1z"/></svg>
        044-555 010 203
      </li>
      <li>
        <svg viewBox="0 0 24 24" aria-hidden="true"><path d="M2 5h20v14H2z M2 5l10 8 10-8" fill="none" stroke="#1f9a3c" stroke-width="0"/><path d="M2 5h20l-10 8z M2 7l10 8 10-8v12H2z"/></svg>
        hello@brightpine.com
      </li>
      <li>
        <svg viewBox="0 0 24 24" aria-hidden="true"><circle cx="12" cy="12" r="10"/><path d="M2 12h20M12 2c3 3 3 17 0 20M12 2c-3 3-3 17 0 20M4 7h16M4 17h16" fill="none" stroke="#ffffff" stroke-width="1.2"/></svg>
        <span>www.<span class="accent">brightpinecompany</span>.com</span>
      </li>
    </ul>
  </div>
</section>

<section class="card card--back" aria-label="Business card back">
  <div class="brand">
    <span class="brand__dot"></span>
    <span class="brand__name">Bright pine company</span>
  </div>
  <div class="pledge">
    <span class="pledge__badge" role="img" aria-label="Recyclable badge"></span>
    <p class="pledge__text">FULLY RECYCLABLE AND 100% WOOD</p>
  </div>
</section>

</body>
</html>
```